Brochure for Home Improvement Startup

We need an eye-catching, informative, and easy to read brochure design to help explain our services to our target audience which include baby boomers and seniors.

Baby

```html
<!DOCTYPE html>
<html lang="en">
<head>
<meta charset="utf-8">
<title>HaleHaven Trifold Brochure</title>
<link href="https://fonts.googleapis.com/css2?family=Open+Sans:wght@400;600;700;800&display=swap" rel="stylesheet">
<style>
:root{
  --teal:#3bb3a6;
  --teal-deep:#2c9c90;
  --charcoal:#4a4a4a;
  --slate:#5f5f5f;
  --mist:#e6e6e6;
  --paper:#ffffff;
  --ink:#3d3d3d;
  --soft-ink:#6d6d6d;
}
*{margin:0;padding:0;box-sizing:border-box}
html,body{width:1200px;height:800px;overflow:hidden;background:#dcdcdc;font-family:"Open Sans",Arial,sans-serif}
.brochure{position:absolute;left:0;top:0;width:1200px;height:800px;display:flex}
.panel{position:relative;width:400px;height:800px;overflow:hidden;background:var(--mist)}
.panel-bg{position:absolute;inset:0;width:400px;height:800px}
.brand{position:absolute;display:flex;align-items:center;gap:10px;font-weight:700;font-size:36px;color:var(--slate);letter-spacing:-.5px}
.brand-mark{width:16px;height:16px;background:var(--slate)}

/* panel one */
.focus{position:absolute;left:36px;top:60px;width:330px;color:var(--paper)}
.focus h2{font-size:26px;font-weight:600;padding-bottom:8px;border-bottom:1.5px solid rgba(255,255,255,.85)}
.focus p{margin-top:12px;font-size:13px;line-height:1.55}
.tagline{position:absolute;left:36px;top:330px;color:var(--paper)}
.tagline .lead{font-size:20px}
.tagline .big{font-size:34px;font-weight:700;letter-spacing:1px;line-height:1.1}
.panel-cover-back .brand{left:70px;top:585px}
.call{position:absolute;left:36px;top:680px}
.call .label{font-size:24px;color:var(--teal);letter-spacing:1.5px}
.call .number{font-size:50px;font-weight:700;color:var(--ink);line-height:1.1}

/* panel two */
.headline{position:absolute;left:34px;top:340px;font-weight:800;font-size:40px;line-height:1.05;letter-spacing:.5px}
.headline .dark{color:var(--ink)}
.headline .light{color:var(--paper)}
.contact{position:absolute;left:34px;top:450px;width:330px;color:#f1f1f1}
.contact h3{font-size:20px;font-weight:600;letter-spacing:1px;padding-bottom:6px;border-bottom:1.5px solid rgba(255,255,255,.8);margin-bottom:12px}
.contact-row{display:flex;align-items:flex-start;gap:10px;font-size:12px;letter-spacing:.6px;text-transform:uppercase;margin-bottom:8px}
.contact-row.phone{font-size:18px;letter-spacing:1px}
.contact-row svg{flex:none;margin-top:2px}
.partners{position:absolute;left:34px;top:662px;width:340px;font-size:14px;color:var(--soft-ink);line-height:1.4}
.badges{position:absolute;left:44px;top:742px;display:flex;gap:40px;align-items:center}
.badge{width:70px;height:30px;background:#c9c9c9}
.badge.round{width:40px;height:40px;border-radius:50%;background:#b9d9b0}

/* panel three */
.panel-cover .brand{left:100px;top:40px}
.caption{position:absolute;left:0;top:575px;width:400px;height:72px;background:rgba(59,179,166,.85);color:var(--paper);font-size:12.5px;line-height:1.45;text-align:center;padding:12px 30px}
.site{position:absolute;right:36px;top:718px;font-size:18px;color:var(--soft-ink)}
.site span{color:var(--teal)}
</style>
</head>
<body>
<main class="brochure">

  <section class="panel panel-cover-back">
    <svg class="panel-bg" viewBox="0 0 400 800" aria-hidden="true">
      <path d="M0 0H400V470Q230 500 0 560Z" fill="var(--teal)"/>
      <path d="M0 800V700Q170 600 400 560V800Z" fill="var(--paper)"/>
    </svg>
    <div class="focus">
      <h2>Focus</h2>
      <p>We deliver light home modification service to seniors and boomers so their homes continue to meet their changing needs. Specifically, we provide consultation and aging in place assessments to homeowners, sales, and installation of high quality grab bars, threshold ramps, lighting, and smart home technology as well as ongoing home maintenance through a home “Fitness Plan”.</p>
    </div>
    <div class="tagline">
      <div class="lead">Enhance (and maintain) Your</div>
      <div class="big">LIFELONG HOME</div>
    </div>
    <div class="brand"><span class="brand-mark"></span>HaleHaven</div>
    <div class="call">
      <div class="label">CONTACT US NOW</div>
      <div class="number">206.555.0148</div>
    </div>
  </section>

  <section class="panel panel-contact">
    <svg class="panel-bg" viewBox="0 0 400 800" aria-hidden="true">
      <defs>
        <linearGradient id="workerTone" x1="0" y1="0" x2="1" y2="1">
          <stop offset="0" stop-color="#cfd3d6"/>
          <stop offset=".6" stop-color="#9fb3c4"/>
          <stop offset="1" stop-color="#7e8a93"/>
        </linearGradient>
      </defs>
      <rect x="0" y="0" width="400" height="420" fill="url(#workerTone)" role="img" aria-label="Photo of a smiling technician fitting a new air filter into a ceiling vent"/>
      <path d="M0 320Q200 300 400 240V645Q200 645 0 630Z" fill="var(--slate)"/>
      <path d="M0 630Q200 645 400 645V800H0Z" fill="var(--mist)"/>
    </svg>
    <div class="headline"><div class="dark">MAKE YOUR</div><div class="light">HOME FIT YOU</div></div>
    <div class="contact">
      <h3>CONTACT US</h3>
      <div class="contact-row">
        <svg width="10" height="14" viewBox="0 0 10 14"><path d="M5 0A5 5 0 0 0 0 5C0 9 5 14 5 14S10 9 10 5A5 5 0 0 0 5 0ZM5 7A2 2 0 1 1 5 3A2 2 0 0 1 5 7Z" fill="#fff"/></svg>
        <span>4810 Harbor Ave SW,<br>Seattle, WA 98126, USA</span>
      </div>
      <div class="contact-row phone">
        <svg width="14" height="14" viewBox="0 0 14 14"><path d="M3 0L5 3L4 5Q5 8 9 10L11 9L14 11L12 14Q6 14 2 9Q0 5 0 2Z" fill="#fff"/></svg>
        <span>206.555.0148</span>
      </div>
      <div class="contact-row">
        <svg width="14" height="10" viewBox="0 0 14 10"><rect width="14" height="10" fill="#fff"/><path d="M0 0L7 6L14 0" stroke="var(--slate)" fill="none"/></svg>
        <span>info@halehavenhome.com</span>
      </div>
      <div class="contact-row">
        <svg width="12" height="12" viewBox="0 0 12 12"><circle cx="6" cy="6" r="5.3" fill="none" stroke="#fff" stroke-width="1.4"/><path d="M0.7 6H11.3M6 0.7V11.3" stroke="#fff"/></svg>
        <span>www.halehavenhome.com</span>
      </div>
    </div>
    <p class="partners">Our vendors, associations, and partners make us a better company. Take a look below to learn more about them.</p>
    <div class="badges">
      <div class="badge"></div>
      <div class="badge round"></div>
      <div class="badge"></div>
    </div>
  </section>

  <section class="panel panel-cover">
    <svg class="panel-bg" viewBox="0 0 400 800" aria-hidden="true">
      <defs>
        <linearGradient id="coupleTone" x1="0" y1="0" x2="1" y2="1">
          <stop offset="0" stop-color="#9a6a55"/>
          <stop offset=".5" stop-color="#b9c3cc"/>
          <stop offset="1" stop-color="#6f9ccf"/>
        </linearGradient>
      </defs>
      <path d="M0 210Q250 190 400 110V650H0Z" fill="url(#coupleTone)" role="img" aria-label="Photo of a smiling senior couple standing in front of their brick home"/>
      <path d="M0 650H400V800H0Z" fill="var(--paper)"/>
    </svg>
    <div class="brand"><span class="brand-mark"></span>HaleHaven</div>
    <p class="caption">To improve the technology, ergonomics, safety, and maintenance of our client's homes to enhance their overall quality of life.</p>
    <div class="site">www.<span>halehavenhome</span>.com</div>
  </section>

</main>
</body>
</html>
```